World Wide Safety Management Product

Hi folks,
We need a website designed for a new product we are launching.

This product is to do with remote Health and Safety Management of people. Combining a wearable device, mobile app and a Portal our Product.

The Product is called 'MyTrekko.Globe' - as it's global and individual. (Trekko are the guides that help & assist you climb Everest)

I've put an initial brief design up to share more of the story with you - http://guardpal.examplehost.net
(I'm not particularly attached to anything on this design - it was something I needed to put together overnight)

We are a software development house and can take your design (in HTML cutup) and work with it - I do need a good creative design though, that will be easy to incorporate into web pages.

For the Initial Design - the landing page will be fine.

For the final design - ideally I'd like the other pages included.

Thank you very much designers unleash your creativity :)

Dave.
Updates

Target Market(s)

Male - 35-60 & females 35-60 working in distributed, decentralised roles for remote companies.

Industry/Entity Type

Media

Logo Text

A friend for life.

Coding

Coded - Design and coding required

Number of Pages Required

4 page

Font styles to use
Other font styles liked:
• 'Open Sans', Arial, Helvetica, sans-serif

Requirements
Must have
• What I'm looking for:
• - ultimate delivery in HTML5/CSS3 - Twitter bootstrap compliant.
• - I need someone who can design + take it through to HTML cutup.
• - creative, I dont want 'more of the same'
• - tells a story simplistically.
Nice to have
• - good use of imagery.
• - good use of white space (sometimes less is best)
Should not have
• Doctors & Nurses running around in imagery.
• We are not a medical provider & we do have plans in the future in this space, but not initially. Focus on the guided safety aspect.

```html
<!DOCTYPE html>
<html lang="en">
<head>
<meta charset="utf-8">
<title>MyTrekko.Globe – Login</title>
<link href="https://fonts.googleapis.com/css2?family=Nunito+Sans:wght@400;600;700;800&display=swap" rel="stylesheet">
<style>
  :root {
    --teal-bg: #17a597;
    --teal-bg-dark: #0e8479;
    --teal-bg-light: #2cb5a8;
    --social-btn: #10a08f;
    --social-btn-icon: #0b8a7b;
    --login-btn: #00b6a0;
    --card: #ffffff;
    --field: #f1f1f1;
    --field-edge: #c9c9c9;
    --text-dark: #333333;
    --text-muted: #8a8a8a;
    --brand-dark: #3a3a3a;
    --white: #ffffff;
  }
  * { box-sizing: border-box; margin: 0; padding: 0; }
  html, body {
    width: 1200px; height: 838px; overflow: hidden;
    font-family: "Nunito Sans", Arial, sans-serif;
  }
  .page { position: relative; width: 1200px; height: 838px; }
  .hero-photo {
    position: absolute; inset: 0;
    background:
      radial-gradient(ellipse at 45% 30%, var(--teal-bg-light) 0%, transparent 45%),
      radial-gradient(ellipse at 80% 70%, var(--teal-bg-dark) 0%, transparent 55%),
      linear-gradient(135deg, var(--teal-bg) 0%, var(--teal-bg-dark) 100%);
  }
  .login-card {
    position: absolute; left: 431px; top: 176px; width: 338px; height: 505px;
    background: var(--card); border-radius: 7px;
  }
  .brand {
    position: absolute; top: 246px; left: 0; right: 0;
    display: flex; justify-content: center; align-items: center; gap: 8px;
  }
  .brand-dot { width: 14px; height: 14px; border-radius: 50%; background: var(--social-btn); }
  .brand-name { font-size: 21px; font-weight: 700; color: var(--brand-dark); letter-spacing: -0.2px; }
  .btn {
    position: absolute; left: 29px; width: 281px; height: 48px; border-radius: 3px;
    color: var(--white); font-weight: 800; font-size: 15.5px; text-transform: uppercase;
    display: flex; align-items: center;
  }
  .btn-social { top: 134px; background: var(--social-btn); }
  .btn-social .btn-icon {
    width: 54px; height: 100%; background: var(--social-btn-icon);
    border-radius: 3px 0 0 3px; display: flex; align-items: center; justify-content: center;
  }
  .btn-social .btn-icon span { width: 12px; height: 12px; background: var(--white); }
  .btn-social .btn-label { flex: 1; text-align: center; }
  .divider-or {
    position: absolute; top: 195px; left: 0; right: 0; text-align: center;
    font-size: 15px; font-weight: 600; color: var(--text-dark);
  }
  .field {
    position: absolute; left: 28px; width: 282px; height: 48px;
    background: var(--field); border: 1px solid #e2e2e2; border-top: 2px solid var(--field-edge);
    border-radius: 3px; padding: 0 10px; display: flex; align-items: center;
    font-size: 11px; color: var(--text-muted);
  }
  .field-username { top: 226px; }
  .field-password { top: 285px; }
  .form-options {
    position: absolute; top: 348px; left: 28px; width: 284px;
    display: flex; justify-content: space-between; align-items: center;
    font-size: 13px; color: var(--text-muted);
  }
  .forgot-link { color: var(--text-muted); text-decoration: underline; }
  .remember { display: flex; align-items: center; gap: 7px; }
  .checkbox { width: 13px; height: 13px; border: 1px solid #c4c4c4; border-radius: 2px; }
  .btn-login { top: 407px; background: var(--login-btn); }
  .btn-login svg { position: absolute; left: 24px; }
  .btn-login .btn-label { flex: 1; text-align: center; font-size: 16px; }
  .follow {
    position: absolute; top: 705px; left: 0; right: 0;
    display: flex; justify-content: center; align-items: center; gap: 12px;
    color: var(--white); font-size: 12px;
  }
  .follow-icon { width: 10px; height: 10px; border-radius: 50%; background: var(--white); }
  .site-footer {
    position: absolute; left: 0; right: 0; top: 760px; height: 78px;
    border-top: 1px solid rgba(255,255,255,0.15); color: var(--white); font-size: 11.5px;
  }
  .copyright { position: absolute; left: 144px; top: 30px; }
  .terms { position: absolute; left: 956px; top: 30px; }
  .version { position: absolute; left: 1170px; top: 30px; }
</style>
</head>
<body>
<div class="page">
  <div class="hero-photo" role="img" aria-label="Teal-toned photo of a professional at work in a café, softly blurred"></div>

  <main class="login-card">
    <div class="brand" style="top:70px">
      <span class="brand-dot"></span>
      <span class="brand-name">mytrekko.globe</span>
    </div>

    <div class="btn btn-social">
      <span class="btn-icon"><span></span></span>
      <span class="btn-label">Login with Friendbook</span>
    </div>

    <div class="divider-or">OR</div>

    <div class="field field-username">Username</div>
    <div class="field field-password">Password</div>

    <div class="form-options">
      <a class="forgot-link" href="#">Forgot Password ?</a>
      <label class="remember"><span class="checkbox"></span>Remember Me</label>
    </div>

    <div class="btn btn-login">
      <svg width="16" height="20" viewBox="0 0 16 20" aria-hidden="true">
        <path d="M4 9V6a4 4 0 0 1 8 0v3" fill="none" stroke="#fff" stroke-width="2.4"/>
        <rect x="0" y="9" width="16" height="11" rx="1.5" fill="#fff"/>
      </svg>
      <span class="btn-label">Login</span>
    </div>
  </main>

  <div class="follow">
    <span>Follow Us :</span>
    <span class="follow-icon"></span>
    <span class="follow-icon"></span>
    <span class="follow-icon"></span>
    <span class="follow-icon"></span>
  </div>

  <footer class="site-footer">
    <span class="copyright">© 2016 Company Name | All Rights Reserved</span>
    <span class="terms">Terms &amp; Conditions</span>
    <span class="version">C5</span>
  </footer>
</div>
</body>
</html>
```